Thornquist Landscaping buisness cards.

There's no existing logo andthis is a new landscaping buisness looking for a complete card design. Would like the logo and name to take up one side.

Target Market(s)

Professionals, Middle aged, Elderly.

Industry/Entity Type

Landscaping

Contact Information for Business Card

Thornquist Landscaping
Malcolm Thornquist (owner)
555-782-4610
Malcolmrthornquist@fernmail.example

Font styles to use
Sans Serif

Colors
9bcb3c
0555a3
ec1f27

Requirements
Must have
• Easy to read print and contact information, all capital letters
Nice to have
• Colored backdrop
Should not have
• Pictures of lawnmowers.

```html
<!DOCTYPE html>
<html lang="en">
<head>
<meta charset="utf-8">
<title>Thornquist Landscaping – Business Cards</title>
<link rel="stylesheet" href="https://fonts.googleapis.com/css2?family=Montserrat:wght@400;500;700&display=swap">
<style>
  :root {
    --page-bg: #8d8e92;
    --card-white: #ffffff;
    --mint-soft: #e9f3dc;
    --mint-mid: #d3e8bd;
    --forest: #0f5a35;
    --bark: #5a3418;
    --ink: #4a2c15;
  }
  * { box-sizing: border-box; margin: 0; padding: 0; }
  html, body { width: 1200px; height: 1000px; overflow: hidden; }
  body {
    background: var(--page-bg);
    font-family: "Montserrat", Arial, sans-serif;
    position: relative;
  }
  .card {
    position: absolute;
    left: 281px;
    width: 639px;
    height: 374px;
    background: var(--card-white);
    overflow: hidden;
  }
  .card--front { top: 107px; }
  .card--back { top: 520px; }
  .card__backdrop {
    position: absolute;
    inset: 0;
    background:
      radial-gradient(ellipse 60% 45% at 15% 95%, var(--mint-mid) 0%, transparent 70%),
      radial-gradient(ellipse 50% 60% at 45% 20%, var(--mint-soft) 0%, transparent 70%),
      radial-gradient(ellipse 40% 50% at 95% 60%, var(--mint-mid) 0%, transparent 70%),
      linear-gradient(160deg, #f4f9ee 0%, #ffffff 45%, #eef6e4 100%);
  }
  .brand-box {
    position: absolute;
    width: 190px;
    height: 192px;
    background: var(--card-white);
    border: 1.5px solid var(--forest);
    display: flex;
    flex-direction: column;
    align-items: center;
    justify-content: center;
    gap: 14px;
  }
  .card--front .brand-box { left: 78px; top: 90px; }
  .card--back .brand-box { left: 224px; top: 91px; }
  .brand-box__square {
    width: 64px;
    height: 64px;
    background: var(--forest);
  }
  .brand-box__name {
    font-weight: 700;
    font-size: 22px;
    line-height: 1.15;
    color: var(--forest);
    text-align: center;
  }
  .contact {
    position: absolute;
    left: 320px;
    top: 130px;
  }
  .contact__name {
    font-weight: 700;
    font-size: 25px;
    color: var(--bark);
    letter-spacing: 0.2px;
  }
  .contact__role {
    font-weight: 500;
    font-size: 17px;
    color: var(--forest);
    margin-top: 2px;
  }
  .contact__list {
    list-style: none;
    margin-top: 22px;
  }
  .contact__item {
    display: flex;
    align-items: center;
    gap: 8px;
    font-size: 13.5px;
    color: var(--ink);
    height: 21px;
  }
  .contact__icon { width: 16px; height: 16px; flex: none; }
</style>
</head>
<body>
  <section class="card card--front">
    <div class="card__backdrop" role="img" aria-label="Soft pale green flowing wave line backdrop"></div>
    <div class="brand-box">
      <div class="brand-box__square"></div>
      <div class="brand-box__name">Thornquist<br>Landscaping</div>
    </div>
    <div class="contact">
      <h1 class="contact__name">Malcolm Thornquist</h1>
      <p class="contact__role">Owner</p>
      <ul class="contact__list">
        <li class="contact__item">
          <svg class="contact__icon" viewBox="0 0 16 16" aria-hidden="true">
            <circle cx="8" cy="8" r="8" fill="#0f5a35"/>
            <path d="M5 11 L11 5" stroke="#fff" stroke-width="2" stroke-linecap="round"/>
          </svg>
          555-782-4610
        </li>
        <li class="contact__item">
          <svg class="contact__icon" viewBox="0 0 16 16" aria-hidden="true">
            <circle cx="8" cy="8" r="8" fill="#0f5a35"/>
            <rect x="4.3" y="5.2" width="7.4" height="5.6" fill="none" stroke="#fff" stroke-width="1.2"/>
            <path d="M4.3 5.4 L8 8.4 L11.7 5.4" fill="none" stroke="#fff" stroke-width="1.2"/>
          </svg>
          Malcolmrthornquist@fernmail.example
        </li>
      </ul>
    </div>
  </section>

  <section class="card card--back">
    <div class="card__backdrop" role="img" aria-label="Soft pale green flowing wave line backdrop"></div>
    <div class="brand-box">
      <div class="brand-box__square"></div>
      <div class="brand-box__name">Thornquist<br>Landscaping</div>
    </div>
  </section>
</body>
</html>
```